Membership Card for our Survival Company

We need a membership card design, front and back for our VIP Membership program. Membership card must be branded with our logo and convey the idea of survivalism.
All members will receive this physical, plastic card with embossed Full Name and unique Membership ID.
ID formatting: "VIP-XXXXXXX"
See example image here:
https://media.pagebrook.net/7k/48b2c91e0a3d5f7e61b8c4d2a9e03f/VIP-Membership-Card1-Reflect.png
Note, this is just an example. We do not require you to follow the size, format, image, etc. The only things that must be included are the:
1) Logo
2) Full Name
3) Membership ID as per the provided format
Any more questions, please let me know.
Industry/Entity Type
It Company
Contact Information for Business Card
Full Name
VIP-XXXXXXX

```html
<!DOCTYPE html>
<html lang="en">
<head>
<meta charset="utf-8">
<title>TrailHardy VIP Membership Card</title>
<link rel="stylesheet" href="https://fonts.googleapis.com/css2?family=Roboto+Slab:wght@700&family=Montserrat:wght@300;600&display=swap">
<style>
  :root {
    --backdrop: #2b2b2b;
    --card-black: #000000;
    --lime: #d4e236;
    --white: #ffffff;
    --brand-orange: #f2a81d;
    --brand-brown: #4a2a08;
    --silver: #cfd2d6;
    --gold: #f4c21f;
  }
  * { box-sizing: border-box; margin: 0; padding: 0; }
  html, body {
    width: 1200px;
    height: 900px;
    overflow: hidden;
    background: var(--backdrop);
  }
  .canvas {
    position: relative;
    width: 1200px;
    height: 900px;
  }
  .card {
    position: absolute;
    width: 560px;
    height: 320px;
    overflow: hidden;
    box-shadow: 0 14px 30px rgba(0, 0, 0, 0.55);
  }
  .card--front {
    left: 80px;
    top: 90px;
    background: var(--card-black);
  }
  .card--back {
    left: 560px;
    top: 480px;
    background: var(--lime);
  }
  .brand {
    position: absolute;
    display: flex;
    align-items: center;
    gap: 12px;
  }
  .brand__dot {
    width: 40px;
    height: 40px;
    border-radius: 50%;
    background: var(--brand-orange);
    flex: none;
  }
  .brand__name {
    font-family: "Roboto Slab", serif;
    font-weight: 700;
    font-size: 38px;
    line-height: 1;
    white-space: nowrap;
  }
  .card--front .brand {
    left: 62px;
    top: 140px;
  }
  .card--front .brand__name { color: var(--brand-orange); }
  .card--back .brand {
    left: 250px;
    top: 250px;
  }
  .card--back .brand__name { color: var(--brand-brown); }
  .checker-field {
    position: absolute;
    left: 0;
    top: 0;
    width: 212px;
    height: 320px;
    background: linear-gradient(135deg, var(--lime), #e8ee9a);
  }
  .panel-black {
    position: absolute;
    left: 146px;
    top: 0;
    width: 414px;
    height: 180px;
    background: var(--card-black);
  }
  .member-name {
    position: absolute;
    left: 214px;
    top: 24px;
    font-family: "Montserrat", sans-serif;
    font-weight: 300;
    font-size: 50px;
    line-height: 1.1;
    letter-spacing: 1px;
    color: var(--silver);
    white-space: nowrap;
  }
  .member-id {
    position: absolute;
    left: 190px;
    top: 108px;
    font-family: "Montserrat", sans-serif;
    font-weight: 600;
    font-size: 38px;
    line-height: 1.1;
    letter-spacing: 3px;
    color: var(--gold);
    white-space: nowrap;
  }
</style>
</head>
<body>
  <main class="canvas">
    <section class="card card--front" aria-label="Membership card front">
      <div class="brand">
        <span class="brand__dot"></span>
        <span class="brand__name">TrailHardy</span>
      </div>
    </section>

    <section class="card card--back" aria-label="Membership card back">
      <div class="checker-field" role="img" aria-label="Lime and white checkered decorative pattern"></div>
      <div class="panel-black"></div>
      <p class="member-name">Full Name</p>
      <p class="member-id">VIP-XXXXXXX</p>
      <div class="brand">
        <span class="brand__dot"></span>
        <span class="brand__name">TrailHardy</span>
      </div>
    </section>
  </main>
</body>
</html>
```